BUSINESS CARD - HALVERDINE RURAL SERVICES

I would like to create a business card for my fertilizer spreading business. I would like to incorporate my existing logo and also a description of the services offered. The business card will be given to farmers so must be kept simple but effective. It will also be left in stores so much also be eye catching in order to stand out from other cards.

Target Market(s)

FARMERS

Requirements
Must have
• FRONT OF CARD = EXISTING LOGO + "CUSTOMISED SPREADING" below the logo

REAR Of CARD = SERVICES OFFERED AND CONTACT DETAILS

- Bulk fertilizer including Lime, Gypsum, Manure & Compost
- Granular fertilizer including Single Super, Urea, Gran-am, & Custom Blends
- Modern equipment - Autosteer & Variable Rate Capable
- Friendly & Reliable Service
- Contact Gus: 0471 502 318
Nice to have
• utilize same color scheme as existing logo

```html
<!DOCTYPE html>
<html lang="en">
<head>
<meta charset="utf-8">
<title>Halverdine Rural Services – Business Card</title>
<link rel="stylesheet" href="https://fonts.googleapis.com/css2?family=Poppins:wght@500;700&family=Montserrat:wght@600&display=swap">
<style>
  :root {
    --slate: #58585c;
    --orange: #f39222;
    --mist: #d6d6d6;
    --paper: #ffffff;
    --ink: #111111;
    --backdrop: #ededed;
  }
  * { margin: 0; padding: 0; box-sizing: border-box; }
  html, body { width: 1200px; height: 1200px; overflow: hidden; }
  body { background: var(--backdrop); position: relative; font-family: "Poppins", sans-serif; }

  .card {
    position: absolute;
    left: 228px;
    width: 744px;
    height: 428px;
    overflow: hidden;
  }
  .card--back { top: 130px; background: var(--paper); }
  .card--front { top: 643px; background: var(--slate); }

  .card__swoosh { position: absolute; inset: 0; width: 744px; height: 428px; }

  .brand { position: absolute; text-align: center; }
  .brand__mark { display: block; margin: 0 auto; border-radius: 50%; }
  .brand__name {
    display: block;
    font-family: "Poppins", sans-serif;
    font-weight: 700;
    white-space: nowrap;
    letter-spacing: -0.3px;
  }

  .card--back .brand { left: 412px; top: 56px; width: 300px; }
  .card--back .brand__mark { width: 92px; height: 92px; background: var(--slate); }
  .card--back .brand__name { margin-top: 12px; font-size: 21px; color: var(--slate); }

  .services {
    position: absolute;
    left: 142px;
    top: 283px;
    list-style: none;
    font-size: 14px;
    font-weight: 500;
    line-height: 17.3px;
    color: var(--ink);
  }
  .services li::before { content: "- "; }

  .card--front .brand { left: 172px; top: 125px; width: 400px; }
  .card--front .brand__mark { width: 112px; height: 112px; background: var(--paper); }
  .card--front .brand__name { margin-top: 14px; font-size: 27px; color: var(--paper); }

  .tagline {
    position: absolute;
    left: 0;
    right: 0;
    top: 378px;
    text-align: center;
    font-family: "Montserrat", sans-serif;
    font-weight: 600;
    font-size: 24px;
    letter-spacing: 1.4px;
    color: var(--paper);
  }
</style>
</head>
<body>

  <section class="card card--back" aria-label="Card reverse: services and contact">
    <svg class="card__swoosh" viewBox="0 0 744 428" aria-hidden="true">
      <path fill="var(--slate)" d="M0 0 H480 C330 40 200 150 104 252 C70 300 30 360 0 428 Z"/>
      <path fill="var(--mist)" d="M104 252 H144 C110 300 88 370 78 428 H0 C30 360 70 300 104 252 Z"/>
      <path fill="var(--orange)" d="M480 0 C330 40 200 150 104 252 H180 C260 120 370 40 480 0 Z"/>
    </svg>

    <div class="brand">
      <span class="brand__mark"></span>
      <span class="brand__name">Halverdine Rural Services</span>
    </div>

    <ul class="services">
      <li>Bulk fertilizer including Lime, Gypsum, Manure &amp; Composts</li>
      <li>Granular fertilizer including Single Super, Urea, Gran-am, &amp; Custom Blends</li>
      <li>Modern equipment</li>
      <li>Friendly &amp; Reliable Service</li>
      <li>Contact Gus: 0471 502 318</li>
    </ul>
  </section>

  <section class="card card--front" aria-label="Card front: brand and tagline">
    <div class="brand">
      <span class="brand__mark"></span>
      <span class="brand__name">Halverdine Rural Services</span>
    </div>
    <p class="tagline">CUSTOMISED SPREADING</p>
  </section>

</body>
</html>
```